R.T. Marlowe Electrical work flyer

I need a flyer design to help generate some extra work. I'm more than happy for a designer to play around with pictures, text, headings, boarders. The flyer will be double sided A4 size.
We specialize in Residential, Commercial, & Industrial Electrical works including PV Solar System Designs & Installations, Maintenance, System Checks & Upgrades, Mains Upgrades, Overhead & Underground, Switchboard Installations & Upgrades, Safety Switches, Spa & Pool connections, LED Lighting solutions, Energy Audit Checks, Fans & Air Conditioning, Hi-bay Lighting, Carpark Lighting, Data Points, Comms Racks, New Home Builds, Office Fitouts ...
We pride ourselves on always doing a great job, guaranteed workmanship, competitive pricing, & leaving the site clean.
Call Derek for a quote on any of your electrical needs
Mobile:0417 386 204
Email: rtmarloweelectrical@vendamail.example
PO Box 58
Brindle Vale VIC 3194

REC: 38071
CEC Accreditation: A3182096

I've added my company logo & some pics, photo's & electrical / solar brand logos that can be used but not a must. I'm more than happy if you can find better pics.

Target Market(s)

Office, Factory & Home Owners

Industry/Entity Type

Electrical

Font styles to use
Serif
Sans Serif

Requirements
Must have
• eye catchy design with not to much information overload.
• Just aiming for people to call up for quotes etc.
Nice to have
• My company logo, electrical & solar works available
Should not have
• pictures of kids

```html
<!DOCTYPE html>
<html lang="en">
<head>
<meta charset="utf-8">
<title>R.T. Marlowe Electrical – Flyer</title>
<link href="https://fonts.googleapis.com/css2?family=Questrial&family=Open+Sans:wght@700&display=swap" rel="stylesheet">
<style>
  :root {
    --page-bg: #f1f1f2;
    --panel-grey: #d1d2d4;
    --ink: #3a3a3c;
    --ink-soft: #2b2b2d;
    --brand-green: #7cc242;
    --mark-green: #5cbf3a;
    --badge-grey: #c4c5c8;
    --white: #ffffff;
  }
  * { margin: 0; padding: 0; box-sizing: border-box; }
  html, body { width: 1200px; height: 862px; overflow: hidden; background: var(--page-bg); }
  body { position: relative; font-family: "Questrial", sans-serif; color: var(--ink); }

  .flyer { position: absolute; top: 73px; width: 517px; height: 730px; background: var(--white);
           box-shadow: 2px 3px 5px rgba(0,0,0,0.35); overflow: hidden; }
  .flyer--front { left: 51px; }
  .flyer--back { left: 632px; }

  .photo { position: absolute; }

  /* front */
  .photo-grid .photo { width: 172px; height: 171px; }
  .cert-line { position: absolute; top: 342px; left: 0; width: 517px; height: 40px; display: flex;
               justify-content: flex-end; gap: 22px; padding-right: 20px; font-size: 13.5px;
               letter-spacing: 0.6px; line-height: 40px; color: var(--ink-soft); }
  .brand-panel { position: absolute; top: 382px; left: 0; width: 517px; height: 192px; background: var(--panel-grey); }
  .brand { position: absolute; display: flex; align-items: center; }
  .brand__dot { border-radius: 50%; background: var(--mark-green); flex: none; }
  .brand__name { color: var(--ink); font-weight: 400; line-height: 1.05; }
  .brand__name span { display: block; }
  .brand--front { left: 36px; top: 42px; }
  .brand--front .brand__dot { width: 108px; height: 108px; margin-right: 30px; }
  .brand--front .brand__name .line-1 { font-size: 42px; letter-spacing: 2px; }
  .brand--front .brand__name .line-2 { font-size: 50px; letter-spacing: 4px; }

  .call-band { position: absolute; top: 589px; left: 0; width: 517px; height: 80px; background: var(--brand-green);
               color: var(--white); text-align: center; }
  .call-band__lead { font-family: "Open Sans", sans-serif; font-weight: 700; font-size: 17px; margin-top: 11px; }
  .call-band__phone { font-size: 27px; margin-top: 4px; letter-spacing: 0.5px; }
  .email-band { position: absolute; top: 684px; left: 0; width: 517px; height: 46px; background: var(--panel-grey);
                text-align: center; font-size: 17px; line-height: 46px; color: var(--ink); }

  /* back */
  .photo-strip .photo { left: 0; width: 121px; height: 122px; }
  .info-panel { position: absolute; left: 136px; top: 0; width: 365px; height: 525px; background: var(--panel-grey); }
  .brand--back { left: 22px; top: 44px; }
  .brand--back .brand__dot { width: 82px; height: 82px; margin-right: 28px; }
  .brand--back .brand__name .line-1 { font-size: 30px; letter-spacing: 1.5px; }
  .brand--back .brand__name .line-2 { font-size: 37px; letter-spacing: 3px; }
  .services { position: absolute; left: 29px; top: 152px; width: 310px; font-size: 17.4px; line-height: 20px;
              text-align: justify; color: var(--ink-soft); }
  .services p + p { margin-top: 20px; }

  .partners { position: absolute; left: 145px; top: 564px; width: 350px; height: 18px; display: flex;
              align-items: center; justify-content: space-between; }
  .partner-badge { height: 12px; border-radius: 2px; background: var(--badge-grey); }

  .contact-band { position: absolute; left: 136px; top: 612px; width: 365px; height: 118px; background: var(--brand-green);
                  color: var(--white); text-align: center; padding-top: 20px; }
  .contact-band__line { font-size: 19px; line-height: 27px; letter-spacing: 0.5px; }
  .contact-band__email { font-size: 15.5px; margin-top: 6px; }
</style>
</head>
<body>

<section class="flyer flyer--front">
  <div class="photo-grid">
    <div class="photo" style="left:0;top:0;background:linear-gradient(180deg,#e4e4e4,#b9b5b1 60%,#7d6a60);" role="img" aria-label="Photo of a bright boardroom with a long polished table and chairs"></div>
    <div class="photo" style="left:172px;top:0;background:linear-gradient(180deg,#2a3548,#3a4452 55%,#6c706c);" role="img" aria-label="Photo of a car park lit by pole lights at night"></div>
    <div class="photo" style="left:344px;top:0;width:173px;background:linear-gradient(180deg,#a4a8ad,#cfd1d2 55%,#e0e0e0);" role="img" aria-label="Photo of a large warehouse with hi-bay lighting"></div>
    <div class="photo" style="left:0;top:171px;background:linear-gradient(180deg,#8fb4dc,#b2c7db 40%,#4c566a 65%,#5e6779);" role="img" aria-label="Photo of rooftop solar panels under blue sky"></div>
    <div class="photo" style="left:172px;top:171px;background:linear-gradient(180deg,#d3cee2,#e0e0e3 45%,#a9a7aa);" role="img" aria-label="Photo of a modern living room with LED lighting"></div>
    <div class="photo" style="left:344px;top:171px;width:173px;background:linear-gradient(180deg,#1a1d2a,#2c3a8a 60%,#222a5e);" role="img" aria-label="Photo of a lit swimming pool at night"></div>
  </div>

  <p class="cert-line"><span>REC: 38071</span><span>CEC Accreditation: A3182096</span></p>

  <div class="brand-panel">
    <div class="brand brand--front">
      <span class="brand__dot"></span>
      <p class="brand__name"><span class="line-1">R.T. Marlowe</span><span class="line-2">Electrical</span></p>
    </div>
  </div>

  <div class="call-band">
    <p class="call-band__lead">Call Derek for a quote on any of your electrical needs</p>
    <p class="call-band__phone">Mobile: 0417 - 386 - 204</p>
  </div>

  <p class="email-band">Email: rtmarloweelectrical@vendamail.example</p>
</section>

<section class="flyer flyer--back">
  <div class="photo-strip">
    <div class="photo" style="top:0;background:linear-gradient(180deg,#c9d1dc,#a3afbf 55%,#dfe0e2);" role="img" aria-label="Photo of a modern lounge interior"></div>
    <div class="photo" style="top:122px;background:linear-gradient(180deg,#c1c3c6,#9aa0aa 50%,#c8cacd);" role="img" aria-label="Photo of a switchboard and comms rack installation"></div>
    <div class="photo" style="top:244px;background:linear-gradient(180deg,#c2b59f,#9a9a94 45%,#5c6578 75%,#aeaeac);" role="img" aria-label="Photo of solar panels on a factory roof"></div>
    <div class="photo" style="top:366px;background:linear-gradient(180deg,#5a4a40,#6e9aa6 50%,#5fa9a0);" role="img" aria-label="Photo of an indoor spa pool with lighting"></div>
    <div class="photo" style="top:488px;background:linear-gradient(180deg,#dcdee0,#eceef0 50%,#c2c7cd);" role="img" aria-label="Photo of an office fitout with ceiling lights"></div>
    <div class="photo" style="top:610px;height:120px;background:linear-gradient(180deg,#d3cee2,#e0e0e3 45%,#a9a7aa);" role="img" aria-label="Photo of a modern living room with LED lighting"></div>
  </div>

  <div class="info-panel">
    <div class="brand brand--back">
      <span class="brand__dot"></span>
      <p class="brand__name"><span class="line-1">R.T. Marlowe</span><span class="line-2">Electrical</span></p>
    </div>
    <div class="services">
      <p>We specialize in Residential, Commercial, &amp; Industrial Electrical works including PV Solar System Designs &amp; Installations, Maintenance, System Checks &amp; Upgrades, Mains Upgrades, Overhead &amp; Underground, Switchboard Installations &amp; Upgrades, Safety Switches, Spa &amp; Pool connections, LED Lighting solutions, Energy Audit Checks, Fans &amp; Air Conditioning, Hi-bay Lighting, Carpark Lighting, Data Points, Comms Racks, New Home Builds, Office Fitouts ...</p>
      <p>We pride ourselves on always doing a great job, guaranteed workmanship, competitive pricing, &amp; leaving the site clean.</p>
    </div>
  </div>

  <div class="partners" aria-label="Partner brands">
    <span class="partner-badge" style="width:56px;"></span>
    <span class="partner-badge" style="width:60px;"></span>
    <span class="partner-badge" style="width:56px;"></span>
    <span class="partner-badge" style="width:52px;"></span>
    <span class="partner-badge" style="width:52px;"></span>
    <span class="partner-badge" style="width:18px;height:18px;"></span>
    <span class="partner-badge" style="width:28px;"></span>
  </div>

  <div class="contact-band">
    <p class="contact-band__line">Brindle Vale VIC 3194</p>
    <p class="contact-band__line">PO Box 58</p>
    <p class="contact-band__email">Email: rtmarloweelectrical@vendamail.example</p>
  </div>
</section>

</body>
</html>
```